Advertising tiles for website

Hi
I have a website at www.plotwren.co.nz and there are four spots along the top for advertising tiles (at the moment there are dummy tiles in place).

Each tile is 220 wide and 200 high and I would like 4 tiles created as a starting point for this site.

I can change the tiles on every page so conceivably we could have very targeted advertising leading the visitor to services we want to promote (we can set this extension up as a new design job for you). Eg. domains for sale, Escrow services, featured domains, Turnkey Websites, New Websites etc.

The advertisements that I might like see on the website would be as follows:
Vellum Forge
Sell Your Domain
Domains For Sale
Featured Domains
Buy Websites
Sell Your Website
Turnkey Websites
Trusted Escrow
New domains
News
Resources
note: the deliverable for this job is 4 tiles (not all of the above)as I want to get the design style sorted with you.

The website where these will appear sells pre-loved domains and turnkey websites. Also, some of these tiles will link through to a classifieds website which we will also want you to help create tiles for once this job is completed to satisfaction.

The files attached are samples only.

Target Market(s)

Domain buyers
Business owners
People buying websites

Industry/Entity Type

Advertising

Requirements
Must have
• Nice clean, clear text
Nice to have
• Fun

```html
<!DOCTYPE html>
<html lang="en">
<head>
<meta charset="utf-8">
<title>Plotwren – Premium Domain Brokers</title>
<link href="https://fonts.googleapis.com/css2?family=Arimo:ital,wght@0,400;0,700;1,400;1,700&family=Titillium+Web:wght@400;700&display=swap" rel="stylesheet">
<style>
:root{
  --red:#a50d14;
  --red-dark:#7c0309;
  --red-deep:#6b0010;
  --maroon:#7a0a0a;
  --grey-tile:#4a4a4a;
  --grey-dark:#2c2c2c;
  --text:#555;
  --link:#a00000;
  --white:#fff;
}
*{margin:0;padding:0;box-sizing:border-box}
html,body{width:1200px;height:1083px;overflow:hidden;background:var(--white)}
body{position:relative;font-family:"Arimo",Arial,sans-serif;color:var(--text)}

.util-bar{position:absolute;left:0;top:0;width:1200px;height:33px;
  background:linear-gradient(#b0141b,var(--red-dark));border-bottom:1px solid #5a0006}
.util-links{position:absolute;right:12px;top:0;display:flex;height:33px;list-style:none}
.util-links li{font-size:12.5px;color:#f3d6d6;line-height:33px;padding:0 12px 0 17px;
  position:relative}
.util-links li::before{content:"";position:absolute;left:0;top:4px;width:1px;height:26px;
  background:#d55;transform:skewX(-20deg)}

.masthead{position:absolute;left:0;top:43px;width:1188px;height:150px;
  background:linear-gradient(90deg,#f4f4f4,#fbfbfb 50%,#f0f0f0);border:1px solid #ddd;overflow:hidden}
.masthead-art{position:absolute;left:2px;top:2px;width:400px;height:146px;
  background:radial-gradient(ellipse at 50% 60%,#c7161f 0%,#b21018 30%,#e4e4e4 62%,#f4f4f4 100%)}
.masthead-wedge{position:absolute;right:0;top:0}
.brand{position:absolute;right:32px;top:96px;font-family:"Arimo",Arial,sans-serif;font-weight:700;
  font-size:36px;letter-spacing:2px;color:var(--white)}

.main-nav{position:absolute;left:0;top:199px;width:1200px;height:39px;
  background:linear-gradient(#c0141c,var(--red-dark));list-style:none}
.main-nav li{position:absolute;top:0;line-height:39px;font-size:16.5px;font-weight:700;color:var(--white)}

.tile{position:absolute;top:261px;width:270px;height:245px;text-align:right;
  font-family:"Titillium Web",sans-serif;color:var(--white);padding-right:16px}
.tile--red{background:radial-gradient(ellipse at 60% 100%,#c21c3e 0%,#8e0c26 55%,var(--red-deep) 100%)}
.tile--grey{background:linear-gradient(#333 0%,#575757 70%,#4e4e4e 100%)}
.tile-title{position:absolute;right:16px;bottom:48px;font-weight:700;font-size:58px;line-height:1;letter-spacing:-1px}
.tile-sub{position:absolute;right:16px;bottom:10px;font-size:36px;line-height:1}
.tile-title--solo{bottom:26px}

.promo-banner{position:absolute;left:0;top:534px;width:1188px;height:206px;
  background:linear-gradient(90deg,#f3eee8 0%,#e9e1d6 40%,#ddd3c6 70%,#e8e2da 100%);border:1px solid #e6e0d8}
.promo-photo{position:absolute;right:0;top:0;width:311px;height:206px;
  background:linear-gradient(120deg,#cfd7de 0%,#e7e5e0 40%,#a39a8e 75%,#4b4540 100%)}
.promo-title{position:absolute;left:18px;top:138px;font-family:"Arimo",Arial,sans-serif;font-style:italic;
  font-size:42px;letter-spacing:-1.5px;color:#9c1010}
.promo-title b{color:#4a4a4a;font-weight:400}

.content{position:absolute;left:12px;top:764px;width:1176px}
.headline{font-size:23px;font-weight:700;color:var(--maroon);line-height:28px}
.content p{font-size:13.5px;line-height:18px}
.content a{color:var(--link)}
.rule{border-top:1px dashed #bbb;margin:0 -4px}
.subhead{font-size:20.5px;font-weight:700;color:#b10c0c;line-height:26px}
.quote em{font-weight:700;color:#555}
.listings{font-size:13.5px;line-height:19.5px;padding-left:48px}
.lead{font-size:24px;font-weight:700;color:var(--maroon);line-height:30px;white-space:nowrap}
.lead a{color:var(--link)}
</style>
</head>
<body>

<header>
  <div class="util-bar">
    <ul class="util-links">
      <li>Home</li><li>Bookmark Site</li><li>Print</li><li>Tell a Friend</li><li>Contact Us</li>
    </ul>
  </div>

  <div class="masthead">
    <div class="masthead-art" role="img" aria-label="Illustration of small figures climbing and pushing large red letters spelling WWW"></div>
    <svg class="masthead-wedge" width="362" height="150" viewBox="0 0 362 150" aria-hidden="true">
      <defs><linearGradient id="wedge" x1="0" y1="0" x2="0" y2="1">
        <stop offset="0" stop-color="#c0121a"/><stop offset="1" stop-color="#8e060c"/></linearGradient></defs>
      <polygon points="0,150 362,0 362,150" fill="url(#wedge)"/>
    </svg>
    <div class="brand">PLOTWREN</div>
  </div>

  <ul class="main-nav">
    <li style="left:22px">Home</li>
    <li style="left:117px">Recent Sales</li>
    <li style="left:269px">Search Listings</li>
    <li style="left:436px">Register New Domain</li>
    <li style="left:653px">Escrow</li>
    <li style="left:757px">FAQ</li>
    <li style="left:839px">Contact Us</li>
  </ul>
</header>

<section class="ad-tiles">
  <div class="tile tile--red" style="left:12px"><span class="tile-title">Sell</span><span class="tile-sub">Your Domain</span></div>
  <div class="tile tile--grey" style="left:310px"><span class="tile-title">Featured</span><span class="tile-sub">Domains</span></div>
  <div class="tile tile--red" style="left:607px"><span class="tile-title">Buy</span><span class="tile-sub">Websites</span></div>
  <div class="tile tile--grey" style="left:905px"><span class="tile-title tile-title--solo">News</span></div>
</section>

<section class="promo-banner">
  <div class="promo-photo" role="img" aria-label="Photo of two business people working together at a laptop in a bright office"></div>
  <div class="promo-title">Premium <b>Domain</b> Brokers</div>
</section>

<main class="content">
  <h2 class="headline">Lumenta.com for sale on Tradeloft</h2>
  <p style="margin-top:7px">Having already changed hands for $20m in 2005 this domain is back on the market.&nbsp; You can <a>read the full story here</a></p>
  <div class="rule" style="margin-top:7px"></div>
  <h2 class="headline" style="margin-top:8px">Plotwren.co.nz Ranked #1 on Seekline NZ Search</h2>
  <h3 class="subhead" style="margin-top:12px">Selling Premium Domains &amp; Websites Since 2003</h3>
  <p class="quote" style="margin-top:12px"><em>"Domains have and will continue to go up in value faster than any other commodity EVER known to man."</em> Hal Brenner, Corvane Corp</p>
  <ul class="listings" style="margin-top:11px">
    <li><a>Browse listings in alphabetical order</a></li>
    <li><a>Browse listings in price order</a></li>
    <li>Looking for something suitable to your industry or interests? <a>Browse listings in category order</a></li>
    <li>Like to know how much domains have been selling for?&nbsp; Check out <a>2010 top international sales</a> and <a>some of NZ's sales</a></li>
  </ul>
  <div class="rule" style="margin-top:17px"></div>
  <p class="lead" style="margin-top:8px">Domain names are virtual real estate and hugely valuable.&nbsp; Check out some <a>recent sales </a> and the <a>top</a></p>
</main>

</body>
</html>
```